Harbor Nightclub

Nightclub flyer., digital single sided, for KV and PX. I included samples of some previous flyers we've used. Sample Info:
HARBOR
FRIDAYS
FRI MAY 1 2020
DJ VORTAN (club floor)
DJ RUZO & DJ TAV (residents on the lounge floor)
4217 Marlow Avenue Sacramento
www.harborvenuehall.example for list/VIP inquiries

Target Market(s)

Upscale top 40 crowd but want some cool and artsy like the examples included.

Font styles to use
Sans Serif

Requirements
Must have
• Harbor Logo
Nice to have
• Would be nice if the flyer can be incorporated later with DJ photos (sometimes we will add dj photos to pixagram etc). Would like a big city type of feel.
Should not have
• Nothing too sexual.

```html
<!DOCTYPE html>
<html lang="en">
<head>
<meta charset="utf-8">
<title>Harbor Nightclub — Friday</title>
<link rel="stylesheet" href="https://fonts.googleapis.com/css2?family=Oswald:wght@300&family=Antonio:wght@200;300&family=Montserrat:wght@400;500&display=swap">
<style>
  :root{
    --ink:#05050a;
    --night:#0b0b22;
    --amber:#5a4216;
    --magenta:#ff3df2;
    --white:#ffffff;
    --frame:#dcec3c;
    --silver-hi:#ffffff;
    --silver-lo:#8d8d8d;
  }
  *{margin:0;padding:0;box-sizing:border-box}
  html,body{width:960px;height:1200px;overflow:hidden;background:var(--ink)}
  .flyer{position:relative;width:960px;height:1200px;overflow:hidden;background:var(--ink);font-family:"Montserrat",sans-serif;color:var(--white)}
  .backdrop{position:absolute;inset:0;
    background:
      radial-gradient(ellipse 260px 420px at 470px 760px, rgba(90,66,22,.55), transparent 70%),
      radial-gradient(ellipse 500px 300px at 760px 180px, rgba(30,30,80,.5), transparent 70%),
      linear-gradient(180deg,#0a0a1c 0%,#08081a 45%,#0d0b0a 75%,#050505 100%);}
  .title-glow{position:absolute;left:140px;top:70px;width:680px;height:320px;
    background:radial-gradient(ellipse at center, rgba(255,61,242,.45) 0%, rgba(255,61,242,.18) 40%, transparent 70%);}
  .title{position:absolute;left:0;right:0;top:118px;text-align:center;
    font-family:"Oswald",sans-serif;font-weight:300;font-size:236px;line-height:1;letter-spacing:2px;
    color:var(--white);
    text-shadow:0 0 8px var(--magenta),0 0 22px var(--magenta),0 0 48px var(--magenta);}
  .venue{position:absolute;left:0;right:0;top:390px;text-align:center;
    font-size:25px;font-weight:500;letter-spacing:.95em;padding-left:.95em}
  .date{position:absolute;left:0;right:0;top:428px;text-align:center;
    font-size:28px;font-weight:500;letter-spacing:.22em;padding-left:.22em}
  .lineup-frame{position:absolute;left:111px;top:545px;width:737px;height:381px;
    border:2px solid var(--frame);border-bottom:none;
    box-shadow:0 0 8px rgba(220,236,60,.6);}
  .dj{position:absolute;font-family:"Antonio",sans-serif;font-weight:200;font-size:118px;line-height:1;
    background:linear-gradient(180deg,var(--silver-hi) 0%,#d9d9d9 40%,var(--silver-lo) 55%,#f2f2f2 100%);
    -webkit-background-clip:text;background-clip:text;color:transparent;white-space:nowrap;letter-spacing:1px}
  .dj--headliner{left:131px;top:606px}
  .dj--residents{right:116px;top:753px}
  .brand{position:absolute;left:0;right:0;top:944px;display:flex;flex-direction:column;align-items:center}
  .brand-dot{width:66px;height:66px;border-radius:50%;background:#b49a3e}
  .brand-name{margin-top:12px;font-size:30px;font-weight:500;letter-spacing:.06em;color:var(--white)}
  .address{position:absolute;left:0;right:0;top:1084px;text-align:center;
    font-size:20px;letter-spacing:.5em;padding-left:.5em}
  .rule{position:absolute;left:303px;top:1131px;width:374px;height:1px;background:rgba(255,255,255,.8)}
  .site{position:absolute;left:0;right:0;top:1147px;text-align:center;
    font-size:19px;letter-spacing:.3em;padding-left:.3em}
</style>
</head>
<body>
<main class="flyer">
  <div class="backdrop" role="img" aria-label="Dark night-time photo of a lit waterfall and foliage behind the flyer"></div>
  <div class="title-glow"></div>
  <h1 class="title">FRIDAY</h1>
  <p class="venue">HARBOR</p>
  <p class="date">MAY•01•2020</p>
  <section class="lineup">
    <div class="lineup-frame"></div>
    <p class="dj dj--headliner">DJ VORTAN</p>
    <p class="dj dj--residents">DJ RUZO &amp; DJ TAV</p>
  </section>
  <div class="brand">
    <span class="brand-dot"></span>
    <span class="brand-name">HARBOR</span>
  </div>
  <p class="address">4217 MARLOW AVENUE SACRAMENTO</p>
  <div class="rule"></div>
  <p class="site">WWW.HARBORVENUEHALL.EXAMPLE</p>
</main>
</body>
</html>
```